Cool business cards

Use my existing logo from sketch harbor (see images I have uploaded) and design a really cool non-stuffy business card. I am a divorce mediator.

```html
<!DOCTYPE html>
<html lang="en">
<head>
<meta charset="utf-8">
<title>Rowan Ellery, J.D. — Business Card</title>
<link rel="stylesheet" href="https://fonts.googleapis.com/css2?family=Montserrat:wght@600;700&family=Questrial&display=swap">
<style>
  :root {
    --stage: #000000;
    --brand-blue: #0a67b0;
    --brand-orange: #f5821f;
    --paper: #ffffff;
    --ink: #555555;
    --muted: #b9c3cc;
  }
  * { margin: 0; padding: 0; box-sizing: border-box; }
  html, body { width: 1200px; height: 998px; overflow: hidden; background: var(--stage); }
  .canvas { position: relative; width: 1200px; height: 998px; }

  .card { position: absolute; left: 261px; width: 680px; height: 389px; }
  .card--front { top: 87px; background: var(--brand-blue); }
  .card--back { top: 522px; background: var(--paper); }

  .mark { position: absolute; border-radius: 50%; }
  .card--front .mark {
    left: 280px; top: 99px; width: 116px; height: 116px;
    background: var(--paper);
  }
  .card--back .mark {
    left: 106px; top: 131px; width: 106px; height: 106px;
    background: var(--brand-blue);
  }
  .mark-name {
    position: absolute; left: 60px; top: 250px; width: 198px; text-align: center;
    font-family: "Montserrat", sans-serif; font-weight: 700; font-size: 15px;
    letter-spacing: 0.5px; color: var(--brand-blue);
  }

  .front-title {
    position: absolute; left: 0; top: 231px; width: 100%; text-align: center;
    font-family: "Montserrat", sans-serif; font-weight: 700; font-size: 25px;
    letter-spacing: 0.6px; color: var(--paper);
  }
  .front-tagline {
    position: absolute; left: 0; top: 259px; width: 100%;
    display: flex; justify-content: center; align-items: center; gap: 8px;
    font-family: "Montserrat", sans-serif; font-weight: 600; font-size: 11px;
    letter-spacing: 0.4px; color: var(--muted);
  }
  .front-tagline .rule { width: 22px; height: 1px; background: var(--muted); }

  .holder-name {
    position: absolute; left: 319px; top: 60px;
    font-family: "Montserrat", sans-serif; font-weight: 700; font-size: 20px;
    color: var(--ink);
  }
  .contact-list { position: absolute; left: 316px; top: 222px; list-style: none; }
  .contact-item {
    display: flex; align-items: center; height: 40px;
    font-family: "Questrial", sans-serif; font-size: 21px; color: var(--ink);
  }
  .contact-item svg { width: 24px; height: 24px; margin-right: 9px; fill: var(--ink); }
</style>
</head>
<body>
<main class="canvas">
  <section class="card card--front">
    <div class="mark" aria-hidden="true"></div>
    <h1 class="front-title">ROWAN ELLERY, J.D.</h1>
    <p class="front-tagline"><span class="rule"></span>DIVORCE &amp; FAMILY MEDIATION<span class="rule"></span></p>
  </section>

  <section class="card card--back">
    <div class="mark" aria-hidden="true"></div>
    <p class="mark-name">ROWAN ELLERY</p>
    <h2 class="holder-name">NAME</h2>
    <ul class="contact-list">
      <li class="contact-item">
        <svg viewBox="0 0 24 24" aria-hidden="true"><path d="M6.6 10.8c1.4 2.8 3.8 5.1 6.6 6.6l2.2-2.2c.3-.3.7-.4 1-.2 1.1.4 2.3.6 3.6.6.6 0 1 .4 1 1V20c0 .6-.4 1-1 1C10.6 21 3 13.4 3 4c0-.6.4-1 1-1h3.5c.6 0 1 .4 1 1 0 1.3.2 2.5.6 3.6.1.3 0 .7-.2 1z"/></svg>
        +00 000000000
      </li>
      <li class="contact-item">
        <svg viewBox="0 0 24 24" aria-hidden="true"><path d="M2 5h20v14H2z M3.5 6.5 12 13l8.5-6.5" fill="none" stroke="#555" stroke-width="0"/><path d="M2 5h20v1.2L12 13 2 6.2z"/><path d="M2 8l10 7 10-7v11H2z"/></svg>
        name@rowanellery.com
      </li>
      <li class="contact-item">
        <svg viewBox="0 0 24 24" aria-hidden="true"><g fill="none" stroke="#555" stroke-width="1.6"><circle cx="12" cy="12" r="9.5"/><ellipse cx="12" cy="12" rx="4.2" ry="9.5"/><path d="M2.5 12h19M4 7h16M4 17h16"/></g></svg>
        www.rowanellery.com
      </li>
    </ul>
  </section>
</main>
</body>
</html>
```